Constructor Company /Carpenter

We need a high quality design for a Brochure up to 8pages.Copmany does plastering, building houses, make renovation of houses.
Updates

Ich brauche zusätzliche Tage um durchzusehen

Target Market(s)

The Brochure is a high quality hand out for architects.

Industry/Entity Type

Construction Company

Font styles to use
Sans Serif

Colors

Designer to choose colors to be used in the design.

Requirements
Must have
• You can build the brochure like the website www.qelvorix.ch is built. The brochure needs to look clean, modern and professionell.
• The brochure need to have the same colors like website www.qelvorix.ch

```html
<!DOCTYPE html>
<html lang="de">
<head>
<meta charset="utf-8">
<title>Qelvorix Bau GmbH – Broschüre</title>
<link href="https://fonts.googleapis.com/css2?family=Montserrat:wght@300;400;600;700;800;900&family=Open+Sans:ital,wght@0,400;0,600;0,700;1,400;1,600&display=swap" rel="stylesheet">
<style>
:root{
  --blue:#1f4ea8;
  --blue-bright:#2f5fd0;
  --paper:#ebebeb;
  --ink:#1c1c1c;
  --dark:rgba(22,22,24,.9);
  --line:#2a55b8;
}
*{box-sizing:border-box;margin:0;padding:0}
html,body{width:1200px;height:4800px;overflow:hidden;background:#fff}
body{position:relative;font-family:"Open Sans",sans-serif;color:var(--ink)}
.page{position:absolute;background:var(--paper);overflow:hidden}
.band-top,.band-bottom{position:absolute;left:0;right:0;background:var(--blue)}
.band-top{top:0;height:32px}
.band-bottom{bottom:0;height:34px}
.photo{position:absolute}
.ph-stone{background:linear-gradient(135deg,#7b8088,#4a4f57 55%,#6a6e74)}
.ph-brick{background:linear-gradient(120deg,#b06a48,#7d4a36 40%,#8a8a88 70%,#5c5c5c)}
.ph-house{background:linear-gradient(180deg,#dfe4e8,#c9ccce 55%,#6c6e6e)}
.ph-house2{background:linear-gradient(180deg,#8fa3b5,#a28a70 45%,#5a4a3d 80%,#2f2f2f)}
.ph-room{background:linear-gradient(180deg,#f2f2f2,#d8d8d8 60%,#bdbdbd)}
.ph-wall{background:linear-gradient(160deg,#a9a59d,#8a877f 50%,#5a6048)}
.ph-garden{background:linear-gradient(180deg,#6f8a5a,#9aa0a0 40%,#c8cccc)}
.ph-pool{background:linear-gradient(160deg,#e9eef2,#2f9be0 45%,#1b6fc0)}
.ph-villa{background:linear-gradient(180deg,#6c8fb8,#9fb6cf 35%,#5b5d5f 65%,#5f8a3c)}
.caption{position:absolute;background:var(--dark);color:#fff;font-style:italic;font-size:10.5px;line-height:1.55;text-align:justify;padding:14px 22px}
.vline{position:absolute;width:3px;background:var(--line)}
.hline{position:absolute;height:3px;background:var(--line)}
.pg-num{position:absolute;top:52px;font-family:"Montserrat",sans-serif;font-weight:300;font-size:52px;letter-spacing:2px;color:var(--blue);line-height:1}
.pg-num span{text-decoration:overline;text-decoration-thickness:3px}
.pg-title{position:absolute;top:135px;font-family:"Montserrat",sans-serif;font-weight:800;font-size:27px;color:var(--blue);line-height:1}
.pg-sub{position:absolute;top:167px;font-family:"Montserrat",sans-serif;font-weight:700;font-size:10px;color:var(--ink);text-transform:uppercase;letter-spacing:-.2px}
.right{right:28px;text-align:right}
.left{left:38px}
.list-head{position:absolute;font-family:"Montserrat",sans-serif;font-weight:700;font-size:10px;color:var(--blue);text-transform:uppercase;line-height:1.3;padding-bottom:8px;border-bottom:2px dotted #9aa6c2}
.list{position:absolute;list-style:none;font-size:10.5px;font-weight:600;line-height:1.75}
.list li::before{content:"• "}
.brand{font-family:"Montserrat",sans-serif;font-weight:400;color:var(--ink);display:flex;align-items:center;gap:12px}
.brand i{display:block;background:var(--blue)}
</style>
</head>
<body>

<!-- Cover -->
<section class="page cover" style="left:250px;top:79px;width:712px;height:1009px">
  <div class="band-top" style="height:38px"></div>
  <div class="brand" style="position:absolute;top:108px;left:0;right:0;justify-content:center;font-size:40px">
    <i style="width:30px;height:30px"></i>Qelvorix Bau GmbH
  </div>
  <div class="photo ph-stone" role="img" aria-label="Hand mit Spachtel beim Verputzen einer Wand" style="left:0;top:210px;width:712px;height:696px"></div>
  <div style="position:absolute;left:67px;top:576px;width:574px;height:371px;background:var(--dark);padding:78px 0 0 44px">
    <div style="font-family:'Montserrat',sans-serif;font-weight:900;font-size:58px;line-height:1.15;color:var(--blue-bright)">IHR GIPSER<br>AUS AESCH IN</div>
    <div style="font-family:'Montserrat',sans-serif;font-weight:700;font-size:35px;color:#fff;margin-top:14px">BASEL UND UMGEBUNG</div>
  </div>
  <div style="position:absolute;top:963px;left:0;right:0;text-align:center;font-size:10px;font-weight:700">www.qelvorix.ch</div>
</section>

<!-- Page 02 -->
<section class="page" style="left:26px;top:1196px;width:548px;height:773px">
  <div class="band-top"></div>
  <div class="photo ph-brick" role="img" aria-label="Hand mit Kelle und Mörtel vor Backsteinmauer" style="left:0;top:32px;width:548px;height:348px"></div>
  <div style="position:absolute;left:0;right:0;top:286px;height:94px;background:var(--dark);padding:14px 0 0 128px;color:#fff;font-family:'Montserrat',sans-serif">
    <div style="font-weight:800;font-size:35px;line-height:1">TRADITION UND</div>
    <div style="font-weight:700;font-size:16px;margin-top:6px">LEIDENSCHAFT</div>
  </div>
  <div class="vline" style="left:62px;top:328px;height:256px"></div>
  <div class="hline" style="left:62px;top:581px;width:62px"></div>
  <p style="position:absolute;left:125px;top:442px;width:372px;font-size:10.5px;font-weight:700;line-height:1.4;text-align:justify">Unsere Auftraggeber profitieren von der Erfahrung die wir in den letzten Jahrzehnten in unserem Handwerk gesammelt haben. Dabei haben wir uns auf Gipser-, Fassaden- und Malerarbeiten spezialisiert.</p>
  <p style="position:absolute;left:125px;top:500px;width:372px;font-size:9px;line-height:1.45;text-align:justify">Unsere Arbeitsweise ermöglicht eine Gerne händigen wir Ihnen unsere einwandfreie termingerechte Ausführung persönliche Referenzen auf Anfrage aus. zu bester Qualität.</p>
  <div class="list-head" style="left:125px;top:578px;width:260px">Was Sie von uns erwarten können:</div>
  <ul class="list" style="left:125px;top:608px">
    <li>Qualitativ einwandfreie Arbeit</li><li>Einhalten der Terminpläne</li><li>Individuelle Beratung</li><li>Detaillierte Kostenaufstellung</li><li>Faires Preis-Leistung Verhältnis</li>
  </ul>
  <div class="band-bottom"></div>
</section>

<!-- Page 03 -->
<section class="page" style="left:637px;top:1196px;width:548px;height:773px">
  <div class="band-top"></div>
  <div class="pg-num right"><span>03</span></div>
  <div class="pg-title right">FASSADEN</div>
  <div class="pg-sub right">Fassaden in Basel, Basel-Land und Aargau</div>
  <div class="photo ph-house" role="img" aria-label="Weisse Hausfassade" style="left:28px;top:200px;width:298px;height:288px"></div>
  <div class="photo ph-house2" role="img" aria-label="Mehrfamilienhaus mit Balkonen" style="left:326px;top:200px;width:192px;height:288px"></div>
  <div class="vline" style="left:28px;top:300px;height:232px"></div>
  <div class="caption" style="left:28px;top:400px;width:298px">Für Ihre Wünsche im Bereich Gipsen und Renovationen sind wir Ihre Fachmänner. Unsere langjährige Berufserfahrung macht uns zum Spezialisten für Ihre Gipsarbeiten im Innen- und Aussenbereich.</div>
  <div class="hline" style="left:28px;top:529px;width:60px"></div>
  <div class="list-head" style="left:86px;top:515px;width:190px">Wir bieten Ihnen folgende Dienstleistungen an:</div>
  <div class="list-head" style="left:330px;top:515px;width:170px">Sie profitieren von:</div>
  <ul class="list" style="left:86px;top:564px"><li>Fassadenputze</li><li>Kellerdämmungen</li><li>Deckendämmungen</li><li>Perimeter-Isolationen</li></ul>
  <ul class="list" style="left:330px;top:564px"><li>Wärmeschutz</li><li>Energieeinsparung</li><li>Schallschutz</li><li>Brandschutz</li><li>schöne Ästhetik</li></ul>
  <div class="band-bottom"></div>
</section>

<!-- Page 04 -->
<section class="page" style="left:26px;top:2025px;width:548px;height:778px">
  <div class="band-top"></div>
  <div class="pg-num left"><span>04</span></div>
  <div class="pg-title left">GIPSEN</div>
  <div class="pg-sub left">Gipserarbeiten in Basel, Basel-Land und Aargau</div>
  <div class="photo ph-room" role="img" aria-label="Frisch verputzter weisser Innenraum" style="left:38px;top:202px;width:300px;height:290px"></div>
  <div class="photo ph-house2" role="img" aria-label="Mehrfamilienhaus mit Balkonen" style="left:338px;top:202px;width:182px;height:290px"></div>
  <div class="vline" style="left:38px;top:300px;height:240px"></div>
  <div class="caption" style="left:38px;top:400px;width:300px">Für Ihre Wünsche im Bereich Gipsen und Renovationen sind wir Ihre Fachmänner. Unsere langjährige Berufserfahrung macht uns zum Spezialisten für Ihre Gipsarbeiten im Innen- und Aussenbereich.</div>
  <div class="hline" style="left:38px;top:537px;width:56px"></div>
  <div class="list-head" style="left:94px;top:530px;width:350px">Wir bieten Ihnen folgende Dienstleistungen an:</div>
  <ul class="list" style="left:94px;top:564px"><li>Gipserarbeiten</li><li>Renovationen</li><li>Dämmungen</li><li>Lehmputze</li><li>Isolationen</li><li>Trockenbau</li><li>Altbausanierungen</li></ul>
  <ul class="list" style="left:282px;top:564px"><li>Fassaden Sanieren</li><li>Diverse Mineralische Abriebe</li><li>Grundputze</li><li>Spachtelungen</li><li>Spezielle Putze</li><li>Kittfugen</li></ul>
  <div class="band-bottom"></div>
</section>

<!-- Page 05 -->
<section class="page" style="left:637px;top:2025px;width:548px;height:778px">
  <div class="band-top"></div>
  <div class="pg-num right"><span>05</span></div>
  <div class="pg-title right">MALEN</div>
  <div class="pg-sub right">Ihr Maler in Basel, Basel-Land und Aargau</div>
  <div class="photo ph-house" role="img" aria-label="Weisse Hausfassade" style="left:25px;top:202px;width:300px;height:290px"></div>
  <div class="photo ph-house2" role="img" aria-label="Mehrfamilienhaus mit Balkonen" style="left:325px;top:202px;width:192px;height:290px"></div>
  <div class="vline" style="left:25px;top:300px;height:240px"></div>
  <div class="caption" style="left:25px;top:400px;width:300px">Für Ihre Wünsche im Bereich Gipsen und Renovationen sind wir Ihre Fachmänner. Unsere langjährige Berufserfahrung macht uns zum Spezialisten für Ihre Gipsarbeiten im Innen- und Aussenbereich.</div>
  <div class="hline" style="left:25px;top:537px;width:62px"></div>
  <div class="list-head" style="left:87px;top:520px;width:190px">Wir bieten Ihnen folgende Aussenarbeiten an:</div>
  <div class="list-head" style="left:325px;top:520px;width:190px">Wir bieten Ihnen folgende Innenarbeiten an:</div>
  <ul class="list" style="left:87px;top:566px"><li>Reinigung</li><li>Neuanstrich</li><li>Spezialfarben</li><li>Beschichtung gegen Schimmelbefall</li><li>Beschichtung gegen Schimmelbefall</li></ul>
  <ul class="list" style="left:325px;top:566px"><li>Malerarbeiten</li><li>Tapezierarbeiten</li><li>Spezialfarben</li><li>Schimmelentfernung</li><li>Beschichtung gegen<br>&nbsp;&nbsp;Schimmelbefall</li></ul>
  <div class="band-bottom"></div>
</section>

<!-- Page 06 -->
<section class="page" style="left:26px;top:2859px;width:548px;height:779px">
  <div class="band-top"></div>
  <div class="pg-num left"><span>06</span></div>
  <div class="pg-title left">UMBAU</div>
  <div class="pg-sub left">Umbau in Basel, Basel-Land und Aargau</div>
  <div class="photo ph-wall" role="img" aria-label="Neue Natursteinmauer im Garten" style="left:38px;top:200px;width:304px;height:290px"></div>
  <div class="photo ph-house2" role="img" aria-label="Mehrfamilienhaus mit Balkonen" style="left:342px;top:200px;width:180px;height:290px"></div>
  <div class="vline" style="left:38px;top:300px;height:240px"></div>
  <div class="caption" style="left:38px;top:400px;width:304px">Fachmännisch erledigen wir für Sie sämtliche Umbauarbeiten. Seit Jahren gehören Renovationen und Umbau zu unserem Fachgebiet.<br>Wir beraten Sie individuell und realisieren Ihre Wünsche.</div>
  <div class="hline" style="left:38px;top:537px;width:56px"></div>
  <div class="list-head" style="left:94px;top:530px;width:350px">Wir bieten Ihnen folgende Dienstleistungen an:</div>
  <ul class="list" style="left:94px;top:564px"><li>Umbau Renovation</li><li>Bad und Küche</li><li>Wandabbruch</li><li>Wandeinzug</li><li>Spitzarbeiten</li></ul>
  <div class="band-bottom"></div>
</section>

<!-- Page 07 -->
<section class="page" style="left:630px;top:2859px;width:555px;height:779px">
  <div class="band-top"></div>
  <div class="pg-num right"><span>07</span></div>
  <div class="pg-title right">GARTENARBEIT</div>
  <div class="pg-sub right">Gartenarbeiten in Basel, Basel-Land und Aargau</div>
  <div class="photo ph-garden" role="img" aria-label="Neu verlegte Gartenplatten" style="left:27px;top:200px;width:305px;height:290px"></div>
  <div class="photo ph-pool" role="img" aria-label="Blau beschichtetes Becken" style="left:332px;top:200px;width:198px;height:145px"></div>
  <div class="photo ph-house2" role="img" aria-label="Mehrfamilienhaus mit Balkonen" style="left:332px;top:345px;width:198px;height:145px"></div>
  <div class="vline" style="left:27px;top:300px;height:232px"></div>
  <div class="caption" style="left:27px;top:408px;width:305px">Unsere Privatkunden schätzen unsere zusätzliche Erfahrung in der Umgebungsarbeit sehr. Daher verwirklichen wir auch Ihre Träume in Ihrem Garten.</div>
  <div class="hline" style="left:27px;top:529px;width:60px"></div>
  <div class="list-head" style="left:87px;top:522px;width:420px">Gerne führen wir für Sie folgende Gartenarbeiten aus:</div>
  <ul class="list" style="left:87px;top:560px"><li>Gartenbau</li><li>Gartenunterhalt</li><li>Gartengestaltung</li><li>Terrassenbegrünung</li><li>Gartenmauer</li><li>Holzterrasse</li><li>Kräuterschneck</li></ul>
  <ul class="list" style="left:240px;top:560px"><li>Sitzplätze</li><li>Überdachung</li><li>Sichtschutz</li><li>Steingarten</li><li>Gartentreppen</li></ul>
  <div class="band-bottom"></div>
</section>

<!-- Back cover -->
<section class="page" style="left:250px;top:3750px;width:712px;height:1013px">
  <div class="band-top" style="height:38px"></div>
  <div class="brand" style="position:absolute;top:72px;left:128px;font-size:22px">
    <i style="width:16px;height:16px"></i>Qelvorix Bau GmbH
  </div>
  <div class="photo ph-villa" role="img" aria-label="Modernes Einfamilienhaus mit Rasen" style="left:0;top:122px;width:712px;height:694px"></div>
  <div style="position:absolute;left:98px;top:200px;width:543px;height:484px;background:var(--dark);padding:34px 28px 0 44px;color:#fff;font-style:italic;font-weight:600;font-size:12.5px;line-height:1.35;text-align:justify">
    <p style="margin-bottom:14px">Unsere Leidenschaft ist es Dinge zu erschaffen und zu verändern, welche Menschen glücklich machen.</p>
    <p style="margin-bottom:14px">Ob der Umbau Ihres Hauses, die Renovation einer charmanten Wohnung oder neue Frische in Ihrem Garten – wir sind Ihr Partner wenn es um handwerkliches Geschick und qualitative Arbeit geht.</p>
    <p style="margin-bottom:14px">Langjährige Erfahrung und vernetztes Denken machen uns zu Ihren effizienten Partnern welches Ihr Bauvorhaben kostenbewusst realisiert. Wir erledigen Arbeiten mit Berufsstolz und Liebe zum Detail.</p>
    <p style="margin-bottom:14px">Unsere Auftraggeber profitieren von der umfangreichen Erfahrung die wir in den letzten Jahrzehnten in verschiedenen Baubereichen gesammelt haben.</p>
    <p style="margin-bottom:14px">So haben wir über die Jahre Erfahrungen gesammelt in den Baubereichen Renovation, Umbau, Fassaden, Isolationen, Trocken und Nassbau und noch vieles mehr.</p>
    <p>Für Sie halten wir ein paar Referenzen auf unserer Webseite bereit. Natürlich freuen wir uns auf Ihre Kontaktaufnahme damit wir Sie gleich selber überzeugen können.</p>
  </div>
  <div class="vline" style="left:118px;top:76px;height:608px"></div>
  <svg style="position:absolute;left:240px;top:852px" width="60" height="70" viewBox="0 0 60 70" aria-hidden="true">
    <path d="M30 4c-11 0-19 8-19 18 0 14 19 32 19 32s19-18 19-32C49 12 41 4 30 4z" fill="none" stroke="var(--blue)" stroke-width="4"/>
    <circle cx="30" cy="22" r="7" fill="none" stroke="var(--blue)" stroke-width="4"/>
    <ellipse cx="30" cy="60" rx="24" ry="6" fill="none" stroke="var(--blue)" stroke-width="3"/>
  </svg>
  <div style="position:absolute;left:312px;top:850px;font-size:9.5px;font-style:italic;font-weight:700;line-height:1.75">
    Lindenweg 8, 4147 Aesch<br>079 000 12 34<br>info@qelvorix.ch<br>www.qelvorix.ch
  </div>
  <div class="band-bottom" style="height:46px"></div>
</section>

</body>
</html>
```